christmas window poster

1 WIndow Poster. Offering Gift Vouchers and Xmas Gift Packs ( products )
Must be eyecatching like :

http://pixelmarketo.net/item/festive-gala-poster-flyer-set/481937?ref=TobiasRennerXK

offer to go on poster:

Buy x2 $100 Gift Vouchers and Get x1 $50 Gift Voucher For Free
Buy x3 $100 Gift Vouchers and Get x1 $100 Gift Voucher For Free
Build Your Own Gift Box & Get a $20 Gift For Free

( small writing somewhere near the bottom )
*Vouchers can not be used to pay for Special Promotions, Products, Luma-Forme Nails or Velvet Strand Hair Extensions.

Target Market(s)

everyone

Industry/Entity Type

Hair

Requirements
Must have
• a cool, modern christmas theme or image.
no old schools images.

```html
<!DOCTYPE html>
<html lang="en">
<head>
<meta charset="utf-8">
<title>Gift Vouchers and Xmas Gift Packs</title>
<link rel="stylesheet" href="https://fonts.googleapis.com/css2?family=Nunito:wght@900&family=Arimo:wght@400;700&display=swap">
<style>
  :root {
    --red-deep: #a3000f;
    --red-mid: #d8101f;
    --red-light: #f04a55;
    --red-panel: #c80f1c;
    --white: #ffffff;
    --ink-red: #b0101c;
    --ink-dark: #3a3a3a;
    --glow: rgba(255, 200, 200, 0.9);
  }
  * { margin: 0; padding: 0; box-sizing: border-box; }
  html, body { width: 849px; height: 1200px; overflow: hidden; }
  body { background: var(--red-deep); }
  .poster {
    position: relative;
    width: 849px;
    height: 1200px;
    overflow: hidden;
    background:
      radial-gradient(ellipse 70% 45% at 50% 30%, var(--red-light) 0%, rgba(240,74,85,0) 70%),
      radial-gradient(ellipse 90% 80% at 50% 55%, var(--red-mid) 0%, var(--red-deep) 100%);
    font-family: "Arimo", Arial, sans-serif;
    color: var(--white);
  }
  .swoosh { position: absolute; inset: 0; width: 849px; height: 1200px; }
  .headline {
    position: absolute;
    top: 62px; left: 0; width: 100%;
    text-align: center;
    font-family: "Nunito", "Arial Rounded MT Bold", sans-serif;
    font-weight: 900;
    line-height: 1.22;
    text-shadow: 0 0 10px var(--glow), 0 0 22px rgba(255,150,150,0.7);
  }
  .headline .line-1 { font-size: 52px; display: block; }
  .headline .line-2 { font-size: 46px; display: block; }
  .offers {
    position: absolute;
    top: 237px; left: 51px;
    width: 747px; height: 212px;
    background: linear-gradient(180deg, #d61623 0%, var(--red-panel) 100%);
    box-shadow: 0 0 24px rgba(255,190,190,0.55);
    text-align: center;
    font-size: 29px;
    line-height: 1.3;
    padding-top: 18px;
  }
  .offers .offer { padding: 0 10px; }
  .offers .divider {
    width: 690px; height: 1px;
    margin: 12px auto 10px;
    background: rgba(255,255,255,0.55);
  }
  .offers strong { font-weight: 700; }
  .or {
    position: absolute;
    top: 464px; left: 0; width: 100%;
    text-align: center;
    font-weight: 700;
    font-size: 32px;
    text-shadow: 0 0 10px var(--glow);
  }
  .gift-box-banner {
    position: absolute;
    top: 527px; left: 185px;
    width: 480px; height: 111px;
  }
  .gift-box-banner svg { position: absolute; inset: 0; }
  .gift-box-banner p {
    position: relative;
    text-align: center;
    color: var(--ink-red);
    font-weight: 700;
    font-size: 31px;
    line-height: 1.3;
    padding-top: 14px;
  }
  .gift-art {
    position: absolute;
    top: 652px; left: 125px;
    width: 588px; height: 488px;
    border: 2px solid rgba(255,255,255,0.75);
    background:
      radial-gradient(ellipse 45% 40% at 50% 52%, #f3e6e2 0%, rgba(243,230,226,0) 100%),
      radial-gradient(ellipse 60% 55% at 48% 45%, #e0202c 0%, #a80c18 100%);
    box-shadow: 0 0 30px rgba(0,0,0,0.25);
  }
  .terms {
    position: absolute;
    bottom: 0; left: 0;
    width: 100%; height: 34px;
    background: var(--white);
    color: var(--ink-dark);
    font-weight: 700;
    font-size: 14px;
    text-align: center;
    line-height: 34px;
  }
</style>
</head>
<body>
<main class="poster">
  <svg class="swoosh" viewBox="0 0 849 1200" aria-hidden="true">
    <path d="M0 40 C220 -10 560 150 849 60 L849 0 L0 0 Z" fill="rgba(255,255,255,0.08)"/>
    <path d="M0 1000 C120 900 80 700 0 620" fill="none" stroke="rgba(255,255,255,0.12)" stroke-width="40"/>
  </svg>

  <h1 class="headline">
    <span class="line-1">Gift Vouchers</span>
    <span class="line-2">and Xmas Gift Packs!</span>
  </h1>

  <section class="offers">
    <p class="offer">Buy x2 $100 Gift Vouchers<br>and <strong>Get x1 $50 Gift Voucher For Free</strong></p>
    <div class="divider"></div>
    <p class="offer">Buy x3 $100 Gift Vouchers<br>and <strong>Get x1 $100 Gift Voucher For Free</strong></p>
  </section>

  <p class="or">or</p>

  <div class="gift-box-banner">
    <svg viewBox="0 0 480 111" width="480" height="111" aria-hidden="true">
      <path d="M4 8 L476 0 L470 108 L0 111 Z" fill="#ffffff"/>
    </svg>
    <p>Build Your Own Gift Box<br>&amp; Get a $20 Gift For Free</p>
  </div>

  <div class="gift-art" role="img" aria-label="Illustration of a white gift box tied with a glossy red ribbon and bow on a red background"></div>

  <p class="terms">Vouchers can not be used to pay for Special Promotions, Products, Luma-Forme Nails or Velvet Strand Hair Extensions</p>
</main>
</body>
</html>
```